New Alcoholic Spiked Seltzer Line

We need a can design for a line of low calorie alcoholic seltzer. This product is a sparkling water and vodka drink with no sugar added in a slim 12 oz can.

This is a lighter, healthier, alternative to the sugary ready-to-drinks on the market. The product contains only 3 ingredients: Vodka, Water and Natural Flavors. It has only 100 calories but still has 5% alcohol, so you don't need to sacrifice alcohol to cut calories.

This product also does not contain any preservatives.

We want this design to communicate the following objectives to the consumer and in this order:

1. Appetizing product
2.Low calorie
3.Communicate the type of beverage (Spiked Seltzer)

The brand name of the product is VELKA.

The flavor of the product needed to be used for the design is Mango-Orange.

Comparable products are:

www.brisavelfizz.example/
https://www.tarnowbubble.example
https://quellrind.example/

The designs should not infringe or copy the creative directions of the products mentionned above. They are only given so that you can better understand the type of product we are developing.

Target Market(s)

Young Professional women between the ages of 25 and 44

Industry/Entity Type

Product

Colors

Designer to choose colors to be used in the design.

Requirements
Must have
• Design extendibility, meaning it can be adapted for other flavors.
• This is a new category in the market we are targeting, so consumers must easily be able to identify what type of product this is.

```html
<!DOCTYPE html>
<html lang="en">
<head>
<meta charset="utf-8">
<title>VELKA Spiked Seltzer – Can Range</title>
<link rel="stylesheet" href="https://fonts.googleapis.com/css2?family=Poppins:wght@300;400;600&display=swap">
<style>
  :root {
    --bg: #ffffff;
    --can-body: #f1efec;
    --can-lid: #dcdad6;
    --can-rim: #e6e4e0;
    --copy-grey: #b3aea8;
    --tagline: #ffffff;
    --mango-orange: #e9442f;
    --blueberry: #1a6d9e;
    --lemon-gold: #d2a52a;
  }
  html, body {
    margin: 0;
    padding: 0;
    width: 1200px;
    height: 1200px;
    overflow: hidden;
    background: var(--bg);
  }
  .can-range {
    display: block;
    width: 1200px;
    height: 1200px;
    font-family: "Poppins", sans-serif;
  }
  .can--mango-orange { color: var(--mango-orange); }
  .can--blueberry { color: var(--blueberry); }
  .can--lemon { color: var(--lemon-gold); }
  .can__lid { fill: var(--can-lid); }
  .can__body { fill: var(--can-body); }
  .can__rim { fill: var(--can-rim); }
  .can__band { fill: currentColor; }
  .can__tagline {
    fill: var(--tagline);
    font-size: 12px;
    font-weight: 400;
    letter-spacing: 1.2px;
  }
  .can__brand {
    fill: currentColor;
    font-size: 150px;
    font-weight: 600;
  }
  .can__copy {
    fill: var(--copy-grey);
    font-size: 12px;
    font-weight: 300;
  }
  .can__abv {
    fill: currentColor;
    font-size: 19px;
    font-weight: 300;
  }
  .can__abv-unit {
    fill: currentColor;
    font-size: 14px;
    font-weight: 300;
  }
</style>
</head>
<body>
<svg class="can-range" viewBox="0 0 1200 1200" xmlns="http://www.w3.org/2000/svg" role="img" aria-label="VELKA spiked seltzer can range in three flavour colours">
  <defs>
    <symbol id="can" viewBox="0 0 342 870" width="342" height="870">
      <!-- lid -->
      <path class="can__lid" d="M22,16 Q171,-4 320,16 L326,32 L16,32 Z"/>
      <!-- body -->
      <path class="can__body" d="M16,32 L326,32 Q342,52 342,96 L342,828 Q342,842 326,852 L16,852 Q0,842 0,828 L0,96 Q0,52 16,32 Z"/>
      <!-- bottom rim -->
      <path class="can__rim" d="M16,852 L326,852 Q318,866 300,868 L42,868 Q24,866 16,852 Z"/>
      <!-- top colour band with wave -->
      <path class="can__band" d="M16,32 L326,32 Q342,52 342,96 L342,192 C300,192 270,156 212,156 C150,156 100,192 0,192 L0,96 Q0,52 16,32 Z"/>
      <!-- bottom colour band -->
      <path class="can__band" d="M0,828 L342,828 L342,842 Q336,852 326,856 L16,856 Q6,852 0,842 Z"/>
      <text class="can__tagline" x="171" y="66" text-anchor="middle">Lighter - Healthier - Alternative</text>
      <text class="can__brand" transform="translate(224,432) rotate(-90)" text-anchor="middle" dominant-baseline="central" textLength="416" lengthAdjust="spacingAndGlyphs">VELKA</text>
      <text class="can__copy" x="171" y="700" text-anchor="middle">Appetizing product Low calorie</text>
      <text class="can__copy" x="171" y="718" text-anchor="middle">Communicate the type of beverage</text>
      <text class="can__copy" x="171" y="737" text-anchor="middle">(Spiked Seltzer)</text>
      <text class="can__abv" x="171" y="795" text-anchor="middle">5.0%</text>
      <text class="can__abv-unit" x="171" y="814" text-anchor="middle">All/ Vol</text>
    </symbol>
  </defs>

  <use class="can--mango-orange" href="#can" x="48" y="144"/>
  <use class="can--blueberry" href="#can" x="429" y="144"/>
  <use class="can--lemon" href="#can" x="810" y="144"/>
</svg>
</body>
</html>
```